Highly rated moving company needs postcard design

We need a highly converting postcard to send when people put their homes for sale online. This should highlight the fact that we're Austin's highest rated moving company, and should convey quality and value. We do local, statewide and long distance moves. We also do office and commerical moves and storage. final design must be sized to work with our mailing system. Please see attached file for more information.

```html
<!DOCTYPE html>
<html lang="en">
<head>
<meta charset="utf-8">
<title>Cedarline Movers Postcard</title>
<link href="https://fonts.googleapis.com/css2?family=Jost:wght@400;500;600;700;800;900&display=swap" rel="stylesheet">
<style>
  :root{
    --navy:#1f1c6e;
    --navy-deep:#17145a;
    --red:#e3141b;
    --red-dark:#a3060c;
    --white:#ffffff;
    --ink:#1b1b1b;
    --stage:#6b6b6b;
    --mail-grey:#efeff2;
  }
  *{box-sizing:border-box;margin:0;padding:0}
  html,body{width:901px;height:1200px;overflow:hidden}
  body{background:var(--stage);font-family:"Jost",sans-serif;position:relative}
  .card{position:absolute;left:71px;width:759px;height:512px;overflow:hidden;background:var(--white)}
  .card--front{top:79px}
  .card--back{top:613px;background:var(--navy)}
  .abs{position:absolute}
  .shapes{position:absolute;left:0;top:0}

  /* front */
  .brand{left:32px;top:30px;width:130px;text-align:center}
  .brand__dot{width:60px;height:56px;border-radius:50%;background:var(--navy);margin:0 auto 4px}
  .brand__name{color:var(--red);font-weight:700;font-size:18px;line-height:18px;letter-spacing:1.5px}
  .brand__name small{display:block;font-size:11px;letter-spacing:5px;line-height:13px}
  .headline{left:21px;top:131px;font-weight:800;font-size:41px;line-height:38px;color:var(--navy);letter-spacing:-.3px}
  .headline span{display:block;color:var(--red-dark)}
  .intro{left:21px;top:213px;width:345px;color:var(--ink)}
  .intro h2{font-size:15px;font-weight:700;line-height:18px}
  .intro p{font-size:11.4px;line-height:15px}
  .family-photo{left:359px;top:0;width:400px;height:310px;background:linear-gradient(90deg,rgba(255,255,255,1) 0%,#d9d4d0 22%,#b9a9a3 50%,#ece8e4 100%)}
  .services{left:261px;top:321px;width:480px;color:var(--white)}
  .services h3{color:var(--red);font-size:18px;font-weight:800;line-height:22px;letter-spacing:.2px}
  .services p{font-size:10.3px;line-height:12.6px;margin-top:4px}
  .service{position:absolute;top:392px;display:flex;align-items:center;color:var(--white);font-size:11px;font-weight:500;line-height:13.5px}
  .service__icon{width:46px;height:46px;border-radius:50%;background:var(--white);border:2px solid var(--red);border-left-color:var(--white);border-bottom-color:var(--white);margin-right:13px;display:flex;align-items:center;justify-content:center}
  .footer-web{left:32px;top:478px;display:flex;align-items:center;gap:8px;color:var(--navy);font-weight:700;font-size:14.5px}
  .footer-div{left:296px;top:473px;width:1px;height:26px;background:#777}
  .licence{left:311px;top:472px;font-size:10px;line-height:13.5px;font-weight:600;color:var(--red)}
  .licence b{color:var(--navy);font-weight:600}
  .phone{display:flex;align-items:center;gap:9px;color:var(--white);font-weight:800}
  .phone--front{left:512px;top:466px;font-size:29px}

  /* back */
  .about{left:27px;top:31px;width:246px;color:var(--white)}
  .section-title{color:var(--red);font-size:17.5px;font-weight:800;line-height:22px;letter-spacing:.2px;white-space:nowrap}
  .about .section-title{font-size:16px}
  .rule{height:1px;background:var(--white);width:150px;margin:7px 0 0;position:relative}
  .rule::before{content:"";position:absolute;left:0;top:-1px;width:77px;height:2px;background:var(--red)}
  .about p{font-size:10.1px;line-height:13.65px;margin-top:11px}
  .crew-photo{left:0;top:255px;width:250px;height:205px;background:linear-gradient(180deg,rgba(31,28,110,0) 0%,rgba(60,56,140,.45) 50%,rgba(31,28,110,0) 100%)}
  .areas{left:27px;top:274px;width:200px;color:var(--white)}
  .areas ul{list-style:none;display:grid;grid-template-columns:84px 100px;grid-auto-flow:column;grid-template-rows:repeat(8,16px);margin-top:5px}
  .areas li{font-size:10.2px;line-height:16px;padding-left:11px;position:relative}
  .areas li::before{content:"";position:absolute;left:0;top:6px;width:4px;height:4px;border-radius:50%;border:1px solid var(--red)}
  .back-web{left:30px;top:438px;color:var(--white);font-size:9px;font-weight:700;letter-spacing:.2px}
  .phone--back{left:28px;top:469px;font-size:28px}
  .values-bar{left:352px;top:0;width:407px;height:38px;background:linear-gradient(90deg,var(--red) 0%,var(--red) 60%,var(--red-dark) 100%);color:var(--white);font-weight:800;font-size:15.8px;line-height:38px;padding-left:38px;letter-spacing:.2px}
  .values-panel{left:362px;top:38px;width:397px;height:278px;background:var(--white)}
  .mail-panel{left:362px;top:316px;width:397px;height:197px;background:var(--mail-grey)}
  .divider-stripe{left:352px;top:38px;width:10px;height:475px;background:var(--white);border-left:3px solid var(--red)}
  .values{left:473px;top:46px;width:248px;color:var(--ink)}
  .values h4{color:var(--red);font-size:11.5px;font-weight:700;line-height:14px}
  .values p{font-size:10.1px;line-height:13.65px}
  .stamp{left:700px;top:333px;width:42px;height:40px;background:#3d3d40}
  .addr-line{left:450px;width:293px;height:1px;background:#9a9aa2}
  .mover-illustration{left:286px;top:28px;width:168px;height:292px;border-radius:80px 80px 20px 20px;background:linear-gradient(160deg,#e24a3d 0%,#c9924f 45%,#6e4a4d 100%)}
  .reviews{left:204px;top:323px;width:210px;height:132px;background:var(--white);border:1px dotted var(--navy);border-radius:4px;padding:4px}
  .reviews__head{background:var(--navy);color:var(--white);font-size:11px;font-weight:700;line-height:20px;border-radius:3px;padding-left:8px}
  .review{margin:6px 4px 0;color:var(--ink)}
  .review h5{font-size:8.5px;font-weight:700;color:var(--navy);line-height:10px}
  .review h5 span{color:var(--red);font-size:6px;letter-spacing:.5px;margin-left:3px}
  .review p{font-size:6.9px;line-height:9.4px}
</style>
</head>
<body>

<!-- FRONT -->
<section class="card card--front">
  <div class="abs family-photo" role="img" aria-label="Photo of a smiling family of three in a bright new home"></div>

  <svg class="shapes" width="759" height="512" viewBox="0 0 759 512">
    <defs>
      <linearGradient id="moverPhotoTone" x1="0" y1="0" x2="1" y2="1">
        <stop offset="0" stop-color="#c9ccd3"/>
        <stop offset="0.5" stop-color="#b89a78"/>
        <stop offset="1" stop-color="#e9e4dd"/>
      </linearGradient>
    </defs>
    <path d="M159 310 H759 V456 H246 C230 400 200 345 159 310 Z" fill="var(--navy)"/>
    <path d="M0 303 C70 285 200 300 240 456 H0 Z" fill="url(#moverPhotoTone)" role="img" aria-label="Photo of a smiling mover carrying a cardboard box"/>
    <path d="M0 297 C80 278 215 296 252 456 L241 456 C205 305 80 290 0 305 Z" fill="var(--red)"/>
    <path d="M470 456 C480 440 490 462 505 461 H759 V512 H450 C455 490 460 470 470 456 Z" fill="var(--red)"/>
    <rect x="0" y="508" width="759" height="4" fill="var(--red)"/>
  </svg>

  <div class="abs brand">
    <div class="brand__dot"></div>
    <div class="brand__name">CEDARLINE<small>MOVERS</small></div>
  </div>

  <h1 class="abs headline">LET OUR FAMILY<span>MOVE YOURS</span></h1>

  <div class="abs intro">
    <h2>Austin Movers</h2>
    <p>Austinites rave about our moving help. We’re proud to be the most dependable moving company in Austin.</p>
  </div>

  <div class="abs services">
    <h3>MOVING SERVICES WE OFFER</h3>
    <p>Whether you’re moving across the street or across the state, we’ll make sure your move is stress-free and efficient. We’ll take care of everything from packing to furniture assembly, so you can relax and focus on your new home.</p>
  </div>

  <div class="service" style="left:262px">
    <div class="service__icon"><svg width="24" height="24" viewBox="0 0 24 24" fill="none" stroke="var(--navy)" stroke-width="1.5"><rect x="4" y="8" width="7" height="13"/><rect x="11" y="3" width="9" height="18"/><path d="M2 21h20M14 7h3M14 11h3M14 15h3M6 12h3M6 16h3"/></svg></div>
    <span>Residential<br>Moving</span>
  </div>
  <div class="service" style="left:395px">
    <div class="service__icon"><svg width="24" height="24" viewBox="0 0 24 24" fill="none" stroke="var(--navy)" stroke-width="1.5"><rect x="6" y="3" width="13" height="18"/><path d="M9 8h7M9 12h7M9 16h4"/><path d="M15 17l5 3" stroke="var(--red)"/></svg></div>
    <span>Commercial<br>Moving</span>
  </div>
  <div class="service" style="left:528px">
    <div class="service__icon"><svg width="24" height="24" viewBox="0 0 24 24" fill="none" stroke="var(--navy)" stroke-width="1.5"><path d="M3 9l9-4 9 4-9 4z"/><path d="M4 10v8l8 4 8-4v-8M12 13v9"/><circle cx="12" cy="5" r="3" stroke="var(--red)"/></svg></div>
    <span>Packing<br>Services</span>
  </div>
  <div class="service" style="left:646px">
    <div class="service__icon"><svg width="24" height="24" viewBox="0 0 24 24" fill="none" stroke="var(--navy)" stroke-width="1.5"><path d="M3 10h18v4H3zM4 10l14-5 3 5"/><path d="M6 14v6M18 14v6M6 12h12"/></svg></div>
    <span>Piano<br>Moving</span>
  </div>

  <div class="abs footer-web">
    <svg width="15" height="15" viewBox="0 0 24 24" fill="none" stroke="var(--red)" stroke-width="1.8"><circle cx="12" cy="12" r="10"/><path d="M2 12h20M12 2c3 3 3 17 0 20M12 2c-3 3-3 17 0 20"/></svg>
    www.cedarlinemoversatx.com
  </div>
  <div class="abs footer-div"></div>
  <div class="abs licence">Our TXDMV# <b>001234567A</b><br>USDOT#<b>7654321</b></div>
  <div class="abs phone phone--front">
    <svg width="20" height="26" viewBox="0 0 20 26" fill="none" stroke="var(--white)" stroke-width="1.6"><rect x="5" y="1" width="11" height="19" rx="2"/><path d="M9 17h3M2 12c-2 4 0 9 5 12"/></svg>
    512-555-0147
  </div>
</section>

<!-- BACK -->
<section class="card card--back">
  <div class="abs crew-photo" role="img" aria-label="Faint photo of a moving crew team"></div>

  <div class="abs values-bar">CORE VALUES IN OUR MOVING COMPANY</div>
  <div class="abs values-panel"></div>
  <div class="abs mail-panel"></div>
  <div class="abs divider-stripe"></div>

  <div class="abs about">
    <h3 class="section-title">ABOUT CEDARLINE MOVERS</h3>
    <div class="rule"></div>
    <p>My story is the same story I’ve heard from countless people from the east coast that now reside here. I came on vacation to visit and when I did, I was amazed by how nice people were here. I went to a taco stand, paid for my food and after everything was done the cashier came up to me and asked me how my day was going. At first I thought this kid was crazy and my knee jerk reaction was to tell this guy I didn’t have any money for him, but after a second it dawned on me that he had no ulterior motives for this conversation and was just being nice.... It was at this moment I knew this was the place I wanted to live and start a family.</p>
  </div>

  <div class="abs areas">
    <h3 class="section-title">AREAS WE SERVE</h3>
    <ul>
      <li>Austin</li><li>Bee Cave</li><li>Buda</li><li>Brushy Creek</li><li>Cedar Park</li><li>Georgetown</li><li>Hutto</li><li>Lakeway</li>
      <li>Leander</li><li>Liberty Hill</li><li>Manchaca</li><li>North Austin</li><li>Pflugerville</li><li>Round Rock</li><li>South Austin</li><li>West Lake Hills</li>
    </ul>
  </div>

  <div class="abs back-web">www.cedarlinemoversatx.com</div>

  <svg class="shapes" width="759" height="512" viewBox="0 0 759 512">
    <path d="M0 463 H250 C285 463 292 490 297 513 H0 Z" fill="var(--red)"/>
  </svg>
  <div class="abs phone phone--back">
    <svg width="20" height="26" viewBox="0 0 20 26" fill="none" stroke="var(--white)" stroke-width="1.6"><rect x="5" y="1" width="11" height="19" rx="2"/><path d="M9 17h3M2 12c-2 4 0 9 5 12"/></svg>
    512-555-0147
  </div>

  <div class="abs mover-illustration" role="img" aria-label="Cartoon mover in a red cap and shirt carrying a cardboard box"></div>

  <div class="abs values">
    <h4>STRONG</h4>
    <p>You can be the nicest, smartest, friendliest guy in the world, however that doesn’t mean anything if you can’t physically move someone.</p>
    <h4 style="margin-top:4px">HONEST</h4>
    <p>We take integrity very seriously here. If someone has an accident they will notify you immediately of any damages and accept responsibility. Our goal is to make absolutely sure that our customers have nothing but complete trust with us as a company.</p>
    <h4 style="margin-top:14px">FUN</h4>
    <p>We take integrity very seriously here. If someone has an accident they will notify you immediately of any damages and accept responsibility. Our goal is to make absolutely sure that our customers have nothing but complete trust with us as a company.</p>
  </div>

  <div class="abs reviews">
    <div class="reviews__head">Customer Reviews &amp; Testimonials</div>
    <div class="review">
      <h5>Dana M.<span>★★★★★</span></h5>
      <p>Marcus and Eli moved my daughter from one apartment in Austin to another. I was not with my daughter when the move occurred, but she was overwhelmed with...</p>
    </div>
    <div class="review">
      <h5>Carla P.<span>★★★★★</span></h5>
      <p>This was my first time using a moving company, and Cedarline Movers was amazing! Specifically, Marcus &amp; Theo! They were personable and efficient. So polite...</p>
    </div>
  </div>

  <div class="abs stamp"></div>
  <div class="abs addr-line" style="top:393px"></div>
  <div class="abs addr-line" style="top:412px"></div>
  <div class="abs addr-line" style="top:432px"></div>
  <div class="abs addr-line" style="top:451px"></div>
  <div class="abs addr-line" style="top:471px"></div>
</section>

</body>
</html>
```